Buch-/E-Book-Cover für einen Thriller
Zielgruppe
Unter dem Pseudonym Merle Voss (Website: www.merle-voss-beispiel.de) veröffentliche ich Thriller zum Zeitgeschehen. (Beispiel: Trandor - ein kalter Handel)
Aufgabenstellung
Für das Ebook und das Taschenbuch des neuen Thrillers „Der Riegel“ benötige ich ein aussagefähiges, eigenständiges und ins Auge fallendes Cover. Die Grafik kann sich in Farbe und Form bewusst von „Trandor“ abheben, der Fokus liegt auf dem Thema des Thrillers. In anhängender .pdf-Datei sind Handlung und Figuren detailliert beschrieben; keine Bange vor der Seitenzahl - jede Figur hat eine eigene Seite :-) , daher die Größe.

```html
<!DOCTYPE html>
<html lang="de">
<head>
<meta charset="utf-8">
<title>Der Riegel – Merle Voss</title>
<link rel="stylesheet" href="https://fonts.googleapis.com/css2?family=Josefin+Sans:wght@100;300;400;600&display=swap">
<style>
  :root {
    --paper: #dcdcdb;
    --paper-light: #e6e6e5;
    --paper-dark: #cfcfce;
    --ink: #111111;
    --title-light: #c9c9c9;
    --accent-red: #6e1414;
  }
  * { margin: 0; padding: 0; box-sizing: border-box; }
  html, body {
    width: 825px;
    height: 1200px;
    overflow: hidden;
    background: var(--paper);
  }
  .cover {
    position: relative;
    width: 825px;
    height: 1200px;
    overflow: hidden;
    background:
      radial-gradient(ellipse at 30% 20%, var(--paper-light) 0%, transparent 60%),
      radial-gradient(ellipse at 75% 85%, var(--paper-dark) 0%, transparent 55%),
      var(--paper);
    font-family: "Josefin Sans", "Helvetica Neue", Arial, sans-serif;
  }
  .author {
    position: absolute;
    top: 145px;
    left: 0;
    width: 100%;
    text-align: center;
    font-weight: 300;
    font-size: 46px;
    line-height: 1;
    letter-spacing: 1px;
    color: var(--ink);
    text-transform: lowercase;
  }
  .artwork {
    position: absolute;
    left: 98px;
    top: 420px;
    width: 620px;
    height: 600px;
  }
  .artwork svg { width: 100%; height: 100%; display: block; }
  .title-wrap {
    display: contents;
    font-size: inherit;
    font-weight: inherit;
  }
  .title {
    position: absolute;
    left: 0;
    width: 100%;
    text-align: center;
    text-transform: uppercase;
    line-height: 1;
  }
  .title-article {
    top: 322px;
    font-weight: 100;
    font-size: 318px;
    letter-spacing: 0;
    color: var(--ink);
    opacity: 0.88;
  }
  .title-noun {
    top: 752px;
    font-weight: 400;
    font-size: 78px;
    letter-spacing: 12px;
    padding-left: 12px;
    color: var(--title-light);
  }
  .genre {
    position: absolute;
    top: 1082px;
    left: 0;
    width: 100%;
    text-align: center;
    font-weight: 300;
    font-size: 44px;
    line-height: 1;
    color: var(--accent-red);
    text-transform: lowercase;
  }
</style>
</head>
<body>
  <main class="cover">
    <p class="author">merle voss</p>

    <div class="artwork" role="img" aria-label="Dunkle Doppelbelichtung: Silhouette eines liegenden Säuglings, oben kahle Bäume, unten ein nebliger Nadelwald">
      <svg viewBox="0 0 620 600" aria-hidden="true">
        <defs>
          <linearGradient id="artShade" x1="0" y1="0" x2="0" y2="1">
            <stop offset="0" stop-color="#6a6a6a" stop-opacity="0.25"/>
            <stop offset="0.3" stop-color="#2b2b2b" stop-opacity="0.85"/>
            <stop offset="0.7" stop-color="#151515" stop-opacity="0.95"/>
            <stop offset="1" stop-color="#444" stop-opacity="0"/>
          </linearGradient>
          <filter id="soften"><feGaussianBlur stdDeviation="16"/></filter>
        </defs>
        <ellipse cx="310" cy="300" rx="285" ry="230" fill="url(#artShade)" filter="url(#soften)"/>
      </svg>
    </div>

    <h1 class="title-wrap">
      <span class="title title-article">Der</span>
      <span class="title title-noun">Riegel</span>
    </h1>

    <p class="genre">thriller</p>
  </main>
</body>
</html>
```